30th Anniversary Poster

Need a 2ft (Wide) X 3ft (Tall) Poster design for a 30th anniversary party that will be used in .  Need the get the logo to be the theme colors (gold).  Overall theme is elegance with gold and black being the main colors.  The background should be black.  Silver can be used as an accent color.  I need the sign to say Welcome and 30th Anniversary.  I need all text to be editable and fonts easily available.
A feel similar to images in this search is pretty close.
https://www.travinqo.example/find?sess=b7d2e90c41fa3318&ref=8K4QWTRB_plXM204XM204&tok=QPLMZNXdr4HwYbcEeRt2Uv:1650321478903&q=gala+event+poster&mode=4&flt=ZRPWk7Tt9pLmr41nQa8VcyXeHd2sBjKuvFgNoLQmRzT5Wp8xHcYbDe3KaNfVgUiJoPq7LrSt6MwXz2BvNcQhYdGeKjLmPoRsTuVwXyZaBcDeFgHiJkLmNoPqRsTuVwXyZaBcDeFgHiJkLmNoPqRsTuVw-3AbCdEfGhIj_KlMnOpQrStUvWxYzAbCdEfGhIjKlMnOpQrStUv-WxYzAbCdEfGhIj_KlMnOp&sb=Q&sk=4&vx=3bLPqRtw8Zn2KXwPmLrHnQsTUvWxYzAbCdEfGhIjKl&vw=1440&vh=900&px=2

```html
<!DOCTYPE html>
<html lang="en">
<head>
<meta charset="utf-8">
<title>Marlow Systems – 30th Anniversary Welcome Poster</title>
<link rel="stylesheet" href="https://fonts.googleapis.com/css2?family=Playfair+Display:wght@500;700&family=Montserrat:wght@400;600&display=swap">
<style>
  :root {
    --purple-light: #a4469f;
    --purple-mid: #8a2a82;
    --purple-deep: #5a1352;
    --purple-shadow: #3d0c38;
    --gold-light: #f3d88a;
    --gold-mid: #d9a94a;
    --gold-deep: #9a6a24;
    --text-gold: #f1d98e;
    --white: #ffffff;
  }
  html, body {
    margin: 0;
    padding: 0;
    width: 872px;
    height: 1200px;
    overflow: hidden;
    background: var(--purple-shadow);
  }
  .poster {
    display: block;
    width: 872px;
    height: 1200px;
  }
  .welcome-title {
    font-family: "Playfair Display", Georgia, serif;
    font-weight: 700;
    font-size: 128px;
    fill: var(--text-gold);
  }
  .anniversary-title {
    font-family: "Playfair Display", Georgia, serif;
    font-weight: 500;
    font-size: 62px;
    fill: var(--text-gold);
  }
  .brand-name {
    font-family: "Montserrat", Arial, sans-serif;
    font-weight: 600;
    font-size: 30px;
    letter-spacing: 2px;
    fill: var(--text-gold);
  }
  .website {
    font-family: "Montserrat", Arial, sans-serif;
    font-weight: 400;
    font-size: 21px;
    fill: var(--white);
  }
</style>
</head>
<body>
<svg class="poster" viewBox="0 0 872 1200" xmlns="http://www.w3.org/2000/svg">
  <defs>
    <radialGradient id="stage-glow" cx="435" cy="560" r="620" gradientUnits="userSpaceOnUse">
      <stop offset="0" stop-color="var(--purple-light)"/>
      <stop offset="0.55" stop-color="var(--purple-mid)"/>
      <stop offset="1" stop-color="var(--purple-deep)"/>
    </radialGradient>
    <linearGradient id="side-shade" x1="0" y1="0" x2="1" y2="0">
      <stop offset="0" stop-color="#2a0626" stop-opacity="0.55"/>
      <stop offset="0.18" stop-color="#2a0626" stop-opacity="0"/>
      <stop offset="0.82" stop-color="#2a0626" stop-opacity="0"/>
      <stop offset="1" stop-color="#2a0626" stop-opacity="0.55"/>
    </linearGradient>
    <linearGradient id="gold-band" x1="0" y1="0" x2="1" y2="0">
      <stop offset="0" stop-color="var(--gold-light)"/>
      <stop offset="0.5" stop-color="var(--gold-mid)"/>
      <stop offset="1" stop-color="var(--gold-deep)"/>
    </linearGradient>
    <linearGradient id="gold-frame" x1="0" y1="0" x2="1" y2="1">
      <stop offset="0" stop-color="var(--gold-light)"/>
      <stop offset="0.45" stop-color="var(--gold-mid)"/>
      <stop offset="0.75" stop-color="var(--gold-deep)"/>
      <stop offset="1" stop-color="var(--gold-light)"/>
    </linearGradient>
    <linearGradient id="footer-gold" x1="0" y1="0" x2="1" y2="0">
      <stop offset="0" stop-color="var(--gold-mid)"/>
      <stop offset="0.35" stop-color="var(--gold-light)"/>
      <stop offset="0.7" stop-color="var(--gold-mid)"/>
      <stop offset="1" stop-color="var(--gold-light)"/>
    </linearGradient>
    <radialGradient id="party-tones" cx="0.5" cy="0.4" r="0.65">
      <stop offset="0" stop-color="#c9a878"/>
      <stop offset="0.5" stop-color="#8a7564"/>
      <stop offset="1" stop-color="#3b3230"/>
    </radialGradient>
    <path id="welcome-arc" d="M -227 1100 A 662 662 0 0 1 1097 1100"/>
    <path id="anniversary-arc" d="M 120 706 A 315 315 0 0 0 750 706"/>
  </defs>

  <!-- Background -->
  <rect class="backdrop" width="872" height="1200" fill="url(#stage-glow)"/>
  <g class="light-beams">
    <polygon points="10,0 120,0 230,1150 60,1150" fill="#ffffff" opacity="0.05"/>
    <polygon points="300,0 380,0 300,700 180,700" fill="#ffffff" opacity="0.05"/>
    <polygon points="520,0 600,0 720,700 600,700" fill="#ffffff" opacity="0.05"/>
    <polygon points="760,0 860,0 820,1150 640,1150" fill="#ffffff" opacity="0.05"/>
    <polygon points="0,300 160,1150 0,1150" fill="#2a0626" opacity="0.18"/>
    <polygon points="872,300 710,1150 872,1150" fill="#2a0626" opacity="0.18"/>
    <polygon points="250,900 435,1150 150,1150" fill="#ffffff" opacity="0.05"/>
    <polygon points="620,900 720,1150 500,1150" fill="#ffffff" opacity="0.05"/>
  </g>
  <rect class="edge-shade" width="872" height="1200" fill="url(#side-shade)"/>

  <!-- Brand -->
  <g class="brand">
    <circle cx="212" cy="128" r="16" fill="var(--text-gold)"/>
    <text class="brand-name" x="240" y="139">MARLOW SYSTEMS</text>
  </g>

  <!-- Welcome headline -->
  <text class="welcome-title">
    <textPath href="#welcome-arc" startOffset="50%" text-anchor="middle" textLength="690" lengthAdjust="spacing">WELCOME</textPath>
  </text>

  <!-- Gold band -->
  <g class="gold-ribbon">
    <rect x="0" y="666" width="872" height="103" fill="url(#gold-band)"/>
    <rect x="0" y="666" width="872" height="4" fill="var(--gold-deep)" opacity="0.6"/>
    <rect x="0" y="765" width="872" height="4" fill="var(--gold-deep)" opacity="0.6"/>
  </g>

  <!-- Medallion with photo -->
  <g class="medallion">
    <ellipse cx="435" cy="703" rx="295" ry="257" fill="var(--purple-mid)"/>
    <ellipse cx="435" cy="703" rx="295" ry="257" fill="none" stroke="var(--gold-mid)" stroke-width="2.5"/>
    <ellipse cx="435" cy="703" rx="277" ry="242" fill="url(#gold-frame)"/>
    <ellipse class="photo-area" cx="435" cy="705" rx="259" ry="220" fill="url(#party-tones)"
             role="img" aria-label="Photo of guests celebrating, raising glasses and throwing gold confetti around a festive table"/>
  </g>

  <!-- Anniversary line -->
  <text class="anniversary-title">
    <textPath href="#anniversary-arc" startOffset="50%" text-anchor="middle" textLength="700" lengthAdjust="spacing">30TH ANNIVERSARY</textPath>
  </text>

  <!-- Footer -->
  <g class="footer">
    <rect x="0" y="1152" width="872" height="48" fill="url(#footer-gold)"/>
    <text class="website" x="436" y="1183" text-anchor="middle">www.marlowsystems.com</text>
  </g>
</svg>
</body>
</html>
```